Taking a Paper and turning into a wonderful White Paper for Prospects and Clients

This is a white paper I need designed. I am including my company brochure so you can see the design/fonts being used and I'm including a white paper created - one that I like very much.

I am "NOT" looking for a cookie cutter white paper. I'm looking for a nice, clean design but with some creativity. Check out the white paper I included and you will get the idea.

Also included:
- the paper to be designed
- the paper to be designed "WITH" suggested design features such as carve outs, call outs and such

A few things I "DO NOT" like:
- images that are cheesy or corny
* people sitting at a table in a meeting
* Buildings

The white paper I included did not use pictures but had more design created by the firm. I like this approach and will probably give something like this more weight but is not required.

Reason: Realized time frame was too tight

Target Market(s)

Higher-End, wealthier clients

Industry/Entity Type

It Company

Requirements
Must have
• I DO NOT want the copy to be bunched together. The layout should flow where the copy is broken in the right spots to make reading easier. If you read a paper and it is just copy, interest is lost by everyone.
• COLORS: you can see from what I have included the colors I use
• My preference are very balanced colors using "clean spacing"

```html
<!DOCTYPE html>
<html lang="en">
<head>
<meta charset="utf-8">
<title>Fiduciary White Paper – Spread</title>
<link href="https://fonts.googleapis.com/css2?family=Ubuntu:ital,wght@0,300;0,400;0,500;1,300;1,400&family=Ubuntu+Condensed&display=swap" rel="stylesheet">
<style>
  :root {
    --backdrop: #bdd3e7;
    --paper-grey: #dcdcdc;
    --navy: #1f2a6b;
    --ink: #4a4a4a;
    --muted: #7b7b7b;
    --accent-red: #c4122f;
    --rule: #9a9a9a;
    --column-dark: #8e8e8e;
    --column-light: #cfcfcf;
  }
  * { box-sizing: border-box; margin: 0; padding: 0; }
  html, body { width: 1200px; height: 900px; overflow: hidden; }
  body {
    background: var(--backdrop);
    font-family: "Ubuntu", sans-serif;
    position: relative;
  }
  .spread {
    position: absolute;
    left: 40px; top: 250px;
    width: 1120px; height: 400px;
    display: flex;
  }
  .page { position: relative; width: 560px; height: 400px; display: flex; overflow: hidden; }

  /* left page */
  .text-panel {
    flex: 0 0 385px; height: 100%;
    background: linear-gradient(90deg, #d6d6d6, var(--paper-grey));
    padding: 30px 26px 0 32px;
    color: var(--ink);
    overflow: hidden;
  }
  .lead-points { list-style: none; margin-bottom: 10px; max-width: 300px; }
  .lead-points li {
    position: relative;
    padding-left: 13px;
    color: var(--navy);
    font-size: 12.5px;
    line-height: 1.25;
    margin-bottom: 9px;
  }
  .lead-points li::before {
    content: "";
    position: absolute; left: 0; top: 6px;
    width: 4px; height: 4px; border-radius: 50%;
    background: var(--accent-red);
  }
  .small {
    font-family: "Ubuntu Condensed", "Ubuntu", sans-serif;
    font-size: 9.4px;
    line-height: 12.4px;
  }
  .two-col { display: flex; gap: 10px; align-items: stretch; }
  .body-copy { flex: 0 0 165px; padding-top: 2px; }
  .body-copy p + p { margin-top: 12px; text-indent: 34px; }
  .sources {
    flex: 0 0 152px;
    border-top: 1.5px dotted var(--rule);
    border-bottom: 1.5px dotted var(--rule);
    padding: 18px 0 14px;
    color: var(--navy);
    overflow-wrap: anywhere;
  }
  .sources p + p { margin-top: 12px; }
  .closing { margin-top: 14px; }

  .pull-column {
    flex: 0 0 175px; height: 100%;
    background: linear-gradient(90deg, #bdbdbd 0%, var(--column-dark) 20%, #a8a8a8 55%, var(--column-light) 92%, #a6a6a6 100%);
    padding: 150px 32px 0 35px;
  }
  .pull-quote {
    font-weight: 300;
    font-size: 11.4px;
    line-height: 1.3;
    color: #f4f4f4;
  }
  .pull-quote em { font-style: italic; }

  /* right page */
  .stone-visual {
    flex: 0 0 188px; height: 100%;
    background: linear-gradient(90deg, #a9a9a9 0%, #dedede 18%, #ececec 60%, #d2d2d2 100%);
  }
  .text-panel.right {
    flex: 0 0 372px;
    background: linear-gradient(90deg, #e3e3e3, #f7f7f7);
    padding: 32px 40px 0 37px;
    color: var(--muted);
  }
  .text-panel.right p { margin-bottom: 22px; }
  .text-panel.right .strong { color: var(--navy); }
  .commitments { list-style: none; margin: -14px 0 24px; color: var(--navy); }
  .commitments li { margin-bottom: 8px; }
  .final-demand { color: var(--navy); }
  .text-panel.right p.after-list { margin-bottom: 10px; }
</style>
</head>
<body>
  <main class="spread">
    <section class="page page-left">
      <div class="text-panel">
        <ul class="lead-points">
          <li>Well, we say, the question is not whether your financial advisor is a fiduciary.</li>
          <li>The question is whether your financial advisor is consistently acting in your best interest.</li>
        </ul>
        <div class="two-col small">
          <div class="body-copy">
            <p>As an investor, you've almost certainly heard talk about the differences between "the fiduciary standard" and "the suitability standard," applied – varyingly -- to advisers, brokers and other financial professionals.</p>
            <p>In fact, most likely you've heard it said -- umpteen times -- that unless your financial advisors are fiduciaries, required by law to adhere to the fiduciary standard, they won't consistently act with your best interests in mind.</p>
          </div>
          <div class="sources">
            <p>From LEDGER WEEKLY, by Dana Merritt:<br>"Why Your Financial Advisor Should Be a Fiduciary"</p>
            <p>From Civic Evening Report, by Owen Hartley:<br>"Why you should make sure your financial advisor abides by the fiduciary standard"<br>https://www.civicreport.org/evening/economy/column-make-sure-financial-adviser-abides-fiduciary-standard</p>
          </div>
        </div>
        <p class="closing small">Nonetheless, some investors may, for any number of reasons, still choose to hire professionals who work under the suitability standard.</p>
      </div>
      <aside class="pull-column">
        <p class="pull-quote">But, the question remains, <em>should you only hire an advisor acting as a fiduciary and avoid those who are not?</em></p>
      </aside>
    </section>

    <section class="page page-right">
      <div class="stone-visual" role="img" aria-label="Photograph of smooth black stones set along raked waves in pale sand"></div>
      <div class="text-panel right small">
        <p>Here at Veritane - where we audit advisers for our clients covering areas such as fees charged, performance delivered, and investments used – we make certain our clients have great advisers.</p>
        <p>But, our paramount demand, made of all the advisers we audit is - <span class="strong">the Financial Advisor "Acts in our client's best interest"</span></p>
        <p>When -- working on your behalf -- we audit the Registered Investment Advisors, Wealth Managers, Private Bankers, Trust Officers, Brokers or whatever other titles the financial professional may have, what concerns us is that they:</p>
        <ul class="commitments">
          <li>be honest with you</li>
          <li>provide you with sound advice</li>
          <li>look out for your best interest</li>
          <li>offer advice for a fair fee, "or" fair compensation;</li>
        </ul>
        <p class="after-list">and then, above all;</p>
        <p class="final-demand">we must be able to verify that your advisors are consistently doing the right things for you.</p>
      </div>
    </section>
  </main>
</body>
</html>
```